A5 Flyer & A3 poster design for Velvet Lobes

Velvet Lobes are a fun new accesories brand based in the UK

Create an A5 Flyer , A4 poster and simple website under construction landing page.

1. A5 Flyer - Portrait

- Hand drawn example attached showing rough layout. To include 6 pictures (attached) in polaroid format hung on a line using pegs.
- Pictures to be cropped to fit in 6 same size boxes.
- Logo attached
- NEW to be written in the same pink as logo.
- Create a background in keeping with the style of the logo and images

2. A4 poster - Portrait

- The same style , colour and font as the Flyer.
- The same six images just bigger.
- Example layout attached.

COPY FOR FLYER

Brand New Quality Clip-on ears
Soft & light weight for comfortable wear
Perfect for parties, festivals & nights out
Available in a variety of quality faux fur colours with sparkle or velour centre
Great for adults or kids

Email: hello@velvetlobes.co.uk
Call: 07913 284 571
Web: www.velvetlobes.co.uk

Target Market(s)

Females 18 - 40

Industry/Entity Type

Construction

Requirements
Must have
• must be modern. no dated flyer backgrounds

```html
<!DOCTYPE html>
<html lang="en">
<head>
<meta charset="utf-8">
<title>Velvet Lobes – A5 Flyer</title>
<link rel="stylesheet" href="https://fonts.googleapis.com/css2?family=Lato:wght@400;700;900&family=Fredoka:wght@600&display=swap">
<style>
  :root {
    --pink: #e8198b;
    --pink-light: #f657b4;
    --ink: #2b2b2b;
    --white: #ffffff;
    --stage: #e6e6e6;
    --board: #a4a4a4;
    --board-dark: #858585;
    --paper: #fbfbfb;
    --tape: rgba(255,255,255,0.62);
  }
  * { box-sizing: border-box; margin: 0; padding: 0; }
  html, body { width: 1200px; height: 1200px; overflow: hidden; background: var(--stage); }
  .flyer {
    position: absolute; left: 194px; top: 30px;
    width: 908px; height: 1275px;
    transform: scale(0.894); transform-origin: top left;
    background: var(--white); overflow: hidden;
    font-family: "Lato", sans-serif; color: var(--ink);
    box-shadow: 0 6px 18px rgba(0,0,0,.25);
  }
  .layer { position: absolute; left: 0; top: 0; width: 908px; height: 1275px; }

  .brand {
    position: absolute; left: 38px; top: 55px;
    font-family: "Lato", sans-serif; font-weight: 900; color: var(--pink);
    font-size: 96px; line-height: 0.95; letter-spacing: -1px;
  }
  .brand span { display: block; }
  .brand span + span { padding-left: 28px; }

  .new-label {
    position: absolute; left: 612px; top: 158px;
    font-family: "Fredoka", sans-serif; font-weight: 600; color: var(--pink);
    font-size: 72px; letter-spacing: 14px;
  }

  .product {
    position: absolute; left: 545px; width: 318px; height: 207px;
    border: 4px solid var(--pink); border-radius: 30px; background: var(--white);
    box-shadow: 0 3px 6px rgba(0,0,0,.15); overflow: hidden; padding: 8px;
  }
  .product--sparkle { top: 250px; }
  .product--velour { top: 480px; }
  .product .swatch { width: 100%; height: 100%; border-radius: 22px; }
  .product--sparkle .swatch { background: radial-gradient(ellipse 70% 80% at 50% 55%, #c48d6a 0, #d9bc98 35%, #efe4d6 62%, #fff 80%); }
  .product--velour .swatch { background: radial-gradient(ellipse 70% 85% at 50% 55%, #9c1426 0, #3a1518 38%, #2a1e1e 60%, #fff 82%); }

  .features { position: absolute; left: 38px; top: 395px; list-style: none; width: 480px; }
  .features li {
    position: relative; padding-left: 35px; font-size: 24px; line-height: 30px; margin-bottom: 18px;
  }
  .features li::before {
    content: ""; position: absolute; left: 0; top: 6px; width: 16px; height: 16px;
    border-radius: 50%; background: var(--pink);
  }

  .gallery {
    position: absolute; left: 0; top: 703px; width: 908px; height: 412px;
    background:
      repeating-linear-gradient(90deg, rgba(255,255,255,.08) 0 2px, rgba(0,0,0,.06) 2px 5px, transparent 5px 11px),
      linear-gradient(180deg, var(--board) 0%, #bdbdbd 50%, var(--board-dark) 100%);
    border-top: 4px solid var(--pink); border-bottom: 4px solid var(--pink);
  }
  .polaroid {
    position: absolute; width: 252px; height: 172px; background: var(--paper);
    box-shadow: 0 4px 10px rgba(0,0,0,.3); padding: 10px 18px 40px;
  }
  .polaroid .photo { width: 100%; height: 100%; }
  .tape {
    position: absolute; width: 70px; height: 26px; background: var(--tape);
    box-shadow: 0 1px 2px rgba(0,0,0,.1);
  }
  .tape--tr { right: -24px; top: -4px; transform: rotate(40deg); }
  .tape--bl { left: -24px; bottom: 2px; transform: rotate(40deg); }
  .p1 { left: 40px;  top: 23px; } .p2 { left: 332px; top: 23px; } .p3 { left: 623px; top: 23px; }
  .p4 { left: 40px;  top: 224px; } .p5 { left: 332px; top: 224px; } .p6 { left: 623px; top: 224px; }
  .p1 .photo { background: linear-gradient(120deg, #5d4636 0%, #c9a488 35%, #e8cdb3 60%, #8a6a52 100%); }
  .p2 .photo { background: linear-gradient(120deg, #d8c2a6 0%, #c49074 40%, #e7d6c1 65%, #3d2f28 100%); }
  .p3 .photo { background: linear-gradient(110deg, #32403c 0%, #7d8a84 25%, #d9b89b 55%, #8a6a4e 100%); }
  .p4 .photo { background: linear-gradient(120deg, #6a3b2c 0%, #c99278 40%, #e6c3a9 65%, #b48c70 100%); }
  .p5 .photo { background: linear-gradient(120deg, #c7a57c 0%, #8a3a44 30%, #efe0c4 55%, #4a372c 100%); }
  .p6 .photo { background: linear-gradient(110deg, #1f2a24 0%, #6e5a44 35%, #d2aa7e 60%, #2d2620 100%); }

  .contact { position: absolute; left: 36px; top: 1132px; list-style: none; color: var(--white); }
  .contact li { display: flex; align-items: center; gap: 18px; font-size: 21px; font-weight: 700; height: 34px; margin-bottom: 8px; }
  .contact svg { width: 30px; height: 30px; flex: none; }

  .tags { position: absolute; left: 672px; top: 1147px; list-style: none; }
  .tags li { position: relative; padding-left: 34px; font-size: 24px; font-weight: 700; color: var(--ink); line-height: 30px; margin-bottom: 13px; }
  .tags li::before { content: ""; position: absolute; left: 0; top: 7px; width: 15px; height: 15px; border-radius: 50%; background: var(--pink); }
</style>
</head>
<body>
<main class="flyer">
  <svg class="layer" viewBox="0 0 908 1275" aria-hidden="true">
    <defs>
      <linearGradient id="pinkSweep" x1="0" y1="0" x2="1" y2="0">
        <stop offset="0" stop-color="#e8198b"/>
        <stop offset=".6" stop-color="#f657b4"/>
        <stop offset="1" stop-color="#e8198b"/>
      </linearGradient>
    </defs>
    <path d="M345,0 H908 V158 C780,95 590,120 292,298 C345,215 370,110 345,0 Z" fill="url(#pinkSweep)"/>
    <path d="M330,0 C400,160 300,365 30,348" fill="none" stroke="#e8198b" stroke-width="3"/>
    <path d="M310,288 C520,150 700,62 820,68" fill="none" stroke="#ffffff" stroke-width="3"/>
    <rect x="0" y="1115" width="908" height="160" fill="url(#pinkSweep)"/>
    <path d="M270,1115 H908 V1195 C800,1285 620,1262 430,1172 C370,1143 320,1125 270,1115 Z" fill="#ffffff"/>
  </svg>

  <h1 class="brand"><span>Velvet</span><span>Lobes</span></h1>
  <p class="new-label">NEW</p>

  <div class="product product--sparkle"><div class="swatch" role="img" aria-label="Pair of beige faux fur clip-on ears with rose-gold sequin centres"></div></div>
  <div class="product product--velour"><div class="swatch" role="img" aria-label="Pair of black faux fur clip-on ears with red velour centres"></div></div>

  <ul class="features">
    <li>Brand New Quality Clip-on ears</li>
    <li>Soft &amp; light weight for comfortable wear</li>
    <li>Perfect for parties, festivals &amp; nights out</li>
    <li>Available in a variety of quality faux fur colours with sparkle or velour centre</li>
    <li>Great for adults or kids</li>
  </ul>

  <section class="gallery">
    <figure class="polaroid p1"><div class="photo" role="img" aria-label="Three friends wearing clip-on ears taking a selfie"></div><span class="tape tape--tr"></span><span class="tape tape--bl"></span></figure>
    <figure class="polaroid p2"><div class="photo" role="img" aria-label="Two friends smiling in pink and black fur ears"></div><span class="tape tape--tr"></span><span class="tape tape--bl"></span></figure>
    <figure class="polaroid p3"><div class="photo" role="img" aria-label="Woman wearing sparkle fur ears by a window"></div><span class="tape tape--tr"></span><span class="tape tape--bl"></span></figure>
    <figure class="polaroid p4"><div class="photo" role="img" aria-label="Woman wearing pink fur ears"></div><span class="tape tape--tr"></span><span class="tape tape--bl"></span></figure>
    <figure class="polaroid p5"><div class="photo" role="img" aria-label="Close-up of cream fur ears with velour centres"></div><span class="tape tape--tr"></span><span class="tape tape--bl"></span></figure>
    <figure class="polaroid p6"><div class="photo" role="img" aria-label="Two friends on a night out wearing fur ears"></div><span class="tape tape--tr"></span><span class="tape tape--bl"></span></figure>
  </section>

  <ul class="contact">
    <li>
      <svg viewBox="0 0 30 30" fill="none" stroke="#fff" stroke-width="2"><circle cx="15" cy="15" r="13"/><ellipse cx="15" cy="15" rx="6" ry="13"/><path d="M2,15 H28 M5,8 H25 M5,22 H25"/></svg>
      www.velvetlobes.co.uk
    </li>
    <li>
      <svg viewBox="0 0 30 30" fill="none" stroke="#fff" stroke-width="2"><circle cx="15" cy="15" r="13"/><rect x="8" y="10" width="14" height="10"/><path d="M8,10 L15,16 L22,10"/></svg>
      hello@velvetlobes.co.uk
    </li>
    <li>
      <svg viewBox="0 0 30 30"><circle cx="15" cy="15" r="14" fill="#fff"/><path d="M10,7 L13,10 L11.5,13 C12.5,15.5 14.5,17.5 17,18.5 L20,17 L23,20 L20.5,23 C14,22 8,16 7,9.5 Z" fill="#e8198b"/></svg>
      07913 284 571
    </li>
  </ul>

  <ul class="tags">
    <li>PLAYFULL</li>
    <li>FUN</li>
  </ul>
</main>
</body>
</html>
```